A layout of a webpage for oil trade platform

I would like to have a desgin of one page webpage (with section scrollling dowin) that woulf present the new product i.e. oil trade platform for wholesale buyers and sellers.
Layout should consist of the sections similar to the given at: https://klinika.pewnywybor.pl/system-zarzadzania-wizytami
However oil industy require more colors and more photo stories than here for doctor.
I. I woul imagine at first below menu a slider with brueg information about the product and its advantages with "more" button next to the prict screen of our platform on different displays (PC and mobile).
II. Bellow the slider I would imagine icons correspoing to the advantages of that plaftorm:
1. Purchase/sale process automation 24/7
2. Access to the best deals
3. Electronic offerings and orderings
4. Transaction status monitoring
5. Data and transaction security
II A) (optional):
In near future we would like to prepare a short video presenation. Hence please prepare a place to display that element here.
At the moment alternatvily please prepare a How it works section that would explan the platform operating process
III. Next secion is about benefits for Oil Purchaser
It can be done either by icons of by text and corresponding grahip for while section.
Benefits:
- Access to cheaper oil
- Convenience of online orders
- Possibility to compare prices on the market
- Transaction history
- Order status monitoring
- Seccurity and transparency of purchase
IV. Next seciont is about benefits for Oil Seller
Benefits:
- New sale channel
- Attracting new clients
- More oil sold
- Transaction security
- Possibility to integrate with distribution infrastructure and logistits for more efficient automation.
V. Contact form
VI. Footer
I would need a layout that that will correspond to the very dynamic logo but I would expect also a clean form, smoth and modern. It has to be proffessional layout with more corporate character.
It can use a paralax features if needed.

```html
<!DOCTYPE html>
<html lang="en">
<head>
<meta charset="utf-8">
<title>Oilvance – Oil Trade Platform</title>
<link href="https://fonts.googleapis.com/css2?family=Open+Sans:wght@400;600;700;800&display=swap" rel="stylesheet">
<style>
:root{
  --navy:#0f1f3f;
  --navy-2:#172a50;
  --orange:#f26522;
  --white:#ffffff;
  --ink:#333333;
  --muted:#6b6b6b;
  --grey-icon:#a9a9a9;
  --blue-label:#1d3f72;
  --rule:#e3e3e3;
  --blush:#f2e0da;
  --field:#efeaea;
  --field-line:#e2d3ce;
  --bar:#e2e2e2;
}
*{margin:0;padding:0;box-sizing:border-box}
html,body{width:691px;height:1200px;overflow:hidden}
body{position:relative;font-family:"Open Sans",Arial,sans-serif;color:var(--ink);background:var(--white)}
.abs{position:absolute}

/* hero */
.hero{left:0;top:0;width:691px;height:269px;background:radial-gradient(circle at 70% 45%,#1a3263 0%,var(--navy) 60%)}
.brand{left:64px;top:18px;display:flex;align-items:center;gap:7px;color:var(--white);font-weight:700;font-size:13px;letter-spacing:.3px}
.brand-dot{width:14px;height:14px;border-radius:50%;background:var(--orange)}
.top-nav{left:428px;top:0;width:263px;height:20px;background:var(--navy-2);border-bottom-left-radius:12px;display:flex;align-items:center;justify-content:center;gap:9px;font-size:6.5px;color:#dfe5f0}
.hero-title{left:64px;top:109px;font-size:14.5px;font-weight:800;line-height:17px;color:var(--white);letter-spacing:.2px}
.hero-title em{font-style:normal;color:var(--orange)}
.hero-text{left:64px;top:151px;width:255px;font-size:7px;line-height:10.5px;color:#d6dcea}
.btn{height:24px;display:flex;align-items:center;justify-content:center;font-size:6.5px;font-weight:700;letter-spacing:.2px}
.btn-light{left:64px;top:206px;width:110px;background:var(--white);color:var(--navy)}
.btn-accent{left:182px;top:206px;width:82px;background:var(--orange);color:var(--white)}
.devices{left:346px;top:84px;width:286px;height:166px;border-radius:4px;background:linear-gradient(135deg,#2a3a5c 0%,#4a5770 45%,#c9d0da 100%)}

/* features */
.features{left:0;top:269px;width:691px;height:123px;display:flex}
.feature{position:relative;flex:none;text-align:center;font-size:6.8px;line-height:10.5px;color:var(--ink);padding-top:29px}
.feature + .feature{border-left:1px solid var(--rule);margin-top:22px;padding-top:10px;height:75px}
.feature svg{display:block;margin:0 auto 18px}
.feature.active{color:var(--blue-label)}
.feature .caret{display:block;margin:-12px auto 9px}

/* purchaser */
.purchaser{left:0;top:392px;width:691px;height:211px}
.purchaser-panel{left:0;top:0;width:311px;height:211px;background:linear-gradient(135deg,#3b3a33,#24231f)}
.purchaser-photo{left:311px;top:0;width:380px;height:211px;background:linear-gradient(120deg,#5b6470 0%,#b9b4a8 45%,#e4d9c6 75%,#9c978c 100%)}
.section-title-light{left:64px;top:20px;padding-bottom:4px;border-bottom:1px solid #bdbdbd;width:148px;color:var(--white);font-size:8.5px;font-weight:700}
.benefit-list{left:64px;top:52px;list-style:none}
.benefit-list li{height:18px;display:flex;align-items:center;gap:8px;font-size:8.2px;font-weight:600;color:var(--white);letter-spacing:.2px}
.benefit-list li::before{content:"";width:5px;height:5px;background:var(--orange);transform:rotate(45deg);margin-left:1px}
.benefit-list li.highlight{color:var(--orange)}

/* seller */
.seller-title{left:0;top:627px;width:691px;text-align:center;font-size:8.5px;font-weight:700;color:#222}
.seller-title em{font-style:normal;color:var(--orange)}
.seller-lead{left:180px;top:647px;width:331px;text-align:center;font-size:6.3px;line-height:8px;color:var(--muted)}
.seller-item{top:690px;width:124px;margin-left:-62px;text-align:center}
.seller-item svg{display:block;margin:0 auto;height:42px}
.seller-item h3{margin-top:14px;font-size:7.5px;font-weight:700;color:#222}
.seller-item.accent h3{color:var(--orange)}
.seller-item p{margin:16px auto 0;width:114px;font-size:6.3px;line-height:10.5px;color:var(--muted)}

/* contact */
.contact{left:0;top:835px;width:691px;height:259px;background:var(--blush)}
.contact-title{left:0;top:56px;width:691px;text-align:center;font-size:10.5px;font-weight:800;color:#333;letter-spacing:.2px}
.contact-lead{left:0;top:74px;width:691px;text-align:center;font-size:7.3px;color:var(--muted)}
.field{height:23px;background:var(--field);border:1px solid var(--field-line);font-size:6.5px;color:#8a8a8a;padding-left:9px;display:flex;align-items:center}
.send{left:292px;top:199px;width:68px;height:24px;border-radius:12px;background:var(--orange);color:var(--white);font-size:8px;font-weight:600;display:flex;align-items:center;justify-content:center;letter-spacing:.4px}

/* footer */
.footer-brand{left:64px;top:1110px;display:flex;align-items:center;gap:6px;font-weight:700;font-size:11px;color:var(--navy)}
.footer-brand .brand-dot{width:12px;height:12px}
.address{left:64px;top:1138px;width:62px;text-align:center;font-size:7px;line-height:10.5px;color:var(--muted)}
.footer-links{list-style:none;font-size:6.3px;line-height:13.6px;color:#8c8c8c;top:1114px}
.bottom-bar{left:0;top:1178px;width:691px;height:22px;background:var(--bar);font-size:6.3px;color:#8c8c8c;padding-left:65px;display:flex;align-items:center}
</style>
</head>
<body>

<header class="abs hero">
  <div class="abs brand"><span class="brand-dot"></span>OILVANCE</div>
  <nav class="abs top-nav"><span>Sign In</span><span>Create an account</span><span>Contact</span><span>for institutions</span></nav>
  <h1 class="abs hero-title">MEET THE PERFECT<br><em>MANAGEMENT</em> SYSTEM VISITS</h1>
  <p class="abs hero-text">You have little time? You spend hours answering phone calls and calling back to the patients? You lose time to remind you of appointments? Automate routine and surprise patients new quality of service. The time saved for this in what you really like!</p>
  <div class="abs btn btn-light">ORDER A PRESENTATION</div>
  <div class="abs btn btn-accent">LEARN MORE</div>
  <div class="abs devices" role="img" aria-label="Platform screenshots shown on a desktop monitor, a laptop, a tablet and a phone"></div>
</header>

<section class="abs features">
  <div class="feature active" style="width:180px">
    <svg width="26" height="24" viewBox="0 0 26 24"><g fill="#f26522"><ellipse cx="7" cy="17" rx="6" ry="2.5"/><rect x="1" y="13" width="12" height="4"/><ellipse cx="7" cy="13" rx="6" ry="2.5" fill="#f58a55"/><ellipse cx="19" cy="19" rx="6" ry="2.5"/><rect x="13" y="5" width="12" height="14"/><ellipse cx="19" cy="5" rx="6" ry="2.5" fill="#f58a55"/><rect x="7" y="3" width="10" height="9"/><ellipse cx="12" cy="3" rx="5" ry="2" fill="#f58a55"/></g></svg>
    <svg class="caret" width="8" height="5" viewBox="0 0 8 5"><path d="M0 0h8L4 5z" fill="#9a9a9a"/></svg>
    PURCHASE/SALE<br>PROCESS AUTOMATION 24/7
  </div>
  <div class="feature" style="width:118px">
    <svg width="24" height="24" viewBox="0 0 24 24"><path d="M2 10h5v12H2zM8 10l5-9c2 0 3 1 3 3l-1 5h6c2 0 3 2 2 3l-2 8c-.5 1.5-1.5 2-3 2H8z" fill="#a9a9a9"/></svg>
    ACCESS TO<br>THE BEST DEALS
  </div>
  <div class="feature" style="width:115px">
    <svg width="24" height="24" viewBox="0 0 24 24"><g fill="#a9a9a9"><rect x="5" y="5" width="14" height="14"/><rect x="2" y="7" width="3" height="1.5"/><rect x="2" y="11" width="3" height="1.5"/><rect x="2" y="15" width="3" height="1.5"/><rect x="19" y="7" width="3" height="1.5"/><rect x="19" y="11" width="3" height="1.5"/><rect x="19" y="15" width="3" height="1.5"/><rect x="8" y="2" width="1.5" height="3"/><rect x="14" y="2" width="1.5" height="3"/><rect x="8" y="19" width="1.5" height="3"/><rect x="14" y="19" width="1.5" height="3"/></g><rect x="8" y="8" width="8" height="8" fill="#fff"/><rect x="9.5" y="9.5" width="5" height="5" fill="#a9a9a9"/></svg>
    ELECTRONIC OFFERINGS<br>AND ORDERINGS
  </div>
  <div class="feature" style="width:116px">
    <svg width="28" height="24" viewBox="0 0 28 24"><rect x="1" y="1" width="26" height="17" rx="1" fill="#a9a9a9"/><rect x="3" y="3" width="22" height="13" fill="#fff"/><rect x="11" y="18" width="6" height="3" fill="#a9a9a9"/><rect x="7" y="21" width="14" height="2" fill="#a9a9a9"/></svg>
    TRANSACTION STATUS<br>MONITORING
  </div>
  <div class="feature" style="width:162px">
    <svg width="26" height="24" viewBox="0 0 26 24"><g fill="#a9a9a9"><ellipse cx="10" cy="4" rx="8" ry="3"/><path d="M2 6c0 2 4 3 8 3s8-1 8-3v4c0 2-4 3-8 3s-8-1-8-3zM2 12c0 2 4 3 8 3s8-1 8-3v4c0 2-4 3-8 3s-8-1-8-3z"/></g><circle cx="19" cy="17" r="5" fill="#fff" stroke="#a9a9a9" stroke-width="2"/><path d="M17 17l1.5 1.5L21 16" stroke="#a9a9a9" stroke-width="1.5" fill="none"/></svg>
    DATA AND<br>TRANSACTION SECURITY
  </div>
</section>

<section class="abs purchaser">
  <div class="abs purchaser-panel"></div>
  <div class="abs purchaser-photo" role="img" aria-label="Close-up of a hand typing on a desk calculator over printed price sheets"></div>
  <h2 class="abs section-title-light">BENEFITS FOR OIL PURCHASER</h2>
  <ul class="abs benefit-list">
    <li>Access to cheaper oil</li>
    <li class="highlight">Convenience of online orders</li>
    <li>Possibility to compare prices on the market</li>
    <li>Transaction history</li>
    <li>Order status monitoring</li>
    <li>Seccurity and transparency of purchase</li>
  </ul>
</section>

<section>
  <h2 class="abs seller-title">BENEFITS FOR <em>OIL SELLER</em></h2>
  <p class="abs seller-lead">Lorem Ipsum text is all well angood toLorem Ipsum all well angood to Lorem Ipsum text is all we psum all well angood to Lorem Ipsum text is all we</p>

  <div class="abs seller-item accent" style="left:122px">
    <svg width="40" height="42" viewBox="0 0 40 42"><rect x="1" y="6" width="38" height="26" fill="#f26522"/><rect x="4" y="9" width="32" height="20" fill="#fff"/><rect x="7" y="11" width="12" height="7" fill="#f26522"/><rect x="21" y="11" width="12" height="7" fill="#f26522"/><rect x="7" y="20" width="12" height="7" fill="#f26522"/><rect x="21" y="20" width="12" height="7" fill="#f26522"/><rect x="17" y="32" width="6" height="4" fill="#f26522"/><rect x="11" y="36" width="18" height="2.5" fill="#f26522"/></svg>
    <h3>New sale channel</h3>
    <p>Lorem Ipsum text is all well angood toLorem Ipsum all well angood to Lorem Ipsum text is all we</p>
  </div>
  <div class="abs seller-item" style="left:270px">
    <svg width="40" height="42" viewBox="0 0 40 42"><path d="M9 4h14l8 8v22H9z" fill="#b3b3b3"/><circle cx="30" cy="32" r="6" fill="#b3b3b3"/><circle cx="30" cy="32" r="2" fill="#fff"/></svg>
    <h3>Attracting new clients</h3>
    <p>Lorem Ipsum text is all well angood toLorem Ipsum all well angood to Lorem Ipsum text is all we</p>
  </div>
  <div class="abs seller-item" style="left:418px">
    <svg width="44" height="42" viewBox="0 0 44 42"><path d="M4 8c6-6 14-4 16 2l-6 4c-3-2-6-2-10-1z" fill="#b3b3b3"/><path d="M14 12l18 2" stroke="#b3b3b3" stroke-width="3"/><path d="M10 14v26M22 40l6-24 6 24M24 32h8" stroke="#b3b3b3" stroke-width="2.5" fill="none"/><rect x="18" y="38" width="22" height="3" fill="#b3b3b3"/></svg>
    <h3>More oil sold</h3>
    <p>Lorem Ipsum text is all well angood toLorem Ipsum all well angood to Lorem Ipsum text is all we</p>
  </div>
  <div class="abs seller-item" style="left:568px">
    <svg width="40" height="42" viewBox="0 0 40 42"><path d="M20 2l16 6v12c0 10-7 17-16 20C11 37 4 30 4 20V8z" fill="#b3b3b3"/><path d="M13 21l5 5 9-10" stroke="#fff" stroke-width="2.5" fill="none"/></svg>
    <h3>Transaction security</h3>
    <p>Lorem Ipsum text is all well angood toLorem Ipsum all well angood to Lorem Ipsum text is all we</p>
  </div>
</section>

<section class="abs contact">
  <svg class="abs" style="left:310px;top:18px" width="30" height="28" viewBox="0 0 30 28"><g fill="none" stroke="#222" stroke-width="1.5"><path d="M2 9c0-5 26-5 26 0v2h-7V8c-4-1-8-1-12 0v3H2z"/><path d="M7 12h16l4 14H3z"/><rect x="11" y="15" width="8" height="7"/><path d="M13 17h4M13 19h4"/></g></svg>
  <h2 class="abs contact-title">YOU HAVE ADDITIONAL QUESTIONS? WANT TO LEARN MORE?</h2>
  <p class="abs contact-lead">Talk to our consultant. Leave your details and we will contact you within 24 hours</p>
  <div class="abs field" style="left:165px;top:105px;width:161px">Name</div>
  <div class="abs field" style="left:331px;top:105px;width:160px">Name</div>
  <div class="abs field" style="left:165px;top:131px;width:161px">Email</div>
  <div class="abs field" style="left:331px;top:131px;width:160px">Telephone</div>
  <div class="abs field" style="left:165px;top:159px;width:326px">When can we contact you?</div>
  <div class="abs send">SEND</div>
</section>

<footer>
  <div class="abs footer-brand"><span class="brand-dot"></span>OILVANCE</div>
  <p class="abs address">ul. Torowa 12/4<br>02-318 Warsaw<br>Poland</p>
  <ul class="abs footer-links" style="left:214px"><li>- New sale channel</li><li>- Attracting new clients</li><li>- More oil sold</li><li>- Transaction security</li></ul>
  <ul class="abs footer-links" style="left:339px"><li>- Access to cheaper oil</li><li>- Convenience of online orders</li><li>- Possibility to compare prices on</li></ul>
  <ul class="abs footer-links" style="left:488px"><li>- Transaction history</li><li>- Order status monitoring</li><li>- Security and transparency of purchase</li></ul>
  <div class="abs bottom-bar">Copyright © 2017 &nbsp; All Rights Reserved. Privacy Policy | Terms &amp; Conditions</div>
</footer>

</body>
</html>
```